Travel Agency Website - Simple General

Need a 7 page simple design that is pretty repetitive. Need to be able to load quickly that is SEO optimized. Trying to give ideas on what they can do, be personal as we are local, but at the same time come across as professional and get information easily with little burden.

- Landing Page
- Brambleton Vacations Page
- Family Trips
- Road Trips from Texas
- Other Destinations
- About Us Page
- Contact Us Page

Target Market(s)

Families

Coding

Coded - Design and coding required

Number of Pages Required

5+ page

Colors

Designer to choose colors to be used in the design.

Requirements
Must have
• Like it to flow easily with our logo. Use that for colors, etc.

```html
<!DOCTYPE html>
<html lang="en">
<head>
<meta charset="utf-8">
<title>About Us | Wander Lane Travel</title>
<link href="https://fonts.googleapis.com/css2?family=Playfair+Display:wght@600;700&family=Nunito+Sans:wght@400;600;700;800&display=swap" rel="stylesheet">
<style>
:root{
  --navy:#0f2444;
  --navy-deep:#0a1a33;
  --gold:#f5a623;
  --cream:#f7f3ec;
  --paper:#ffffff;
  --stone:#ebe7e1;
  --ink:#1c2230;
  --muted:#5d6472;
  --line:#ddd6cb;
}
*{box-sizing:border-box;margin:0;padding:0}
html,body{width:1200px;height:3032px;overflow:hidden}
body{font-family:"Nunito Sans",Arial,sans-serif;color:var(--ink);background:var(--paper)}
h1,h2,h3,.brand{font-family:"Playfair Display",Georgia,serif}

.site-nav{height:68px;display:flex;align-items:center;justify-content:space-between;padding:0 28px;background:var(--paper);border-bottom:1px solid var(--line)}
.brand{font-size:26px;font-weight:700;color:var(--navy)}
.nav-links{display:flex;align-items:center;gap:28px;font-size:15px;font-weight:600;color:var(--ink)}
.nav-links .active{border-bottom:2px solid var(--gold);padding-bottom:3px}
.nav-cta{background:var(--navy);color:#fff;padding:10px 18px;border-radius:5px;font-weight:700}

.hero{position:relative;height:672px;overflow:hidden}
.hero-photo{position:absolute;inset:0;background:linear-gradient(100deg,#6d7a86 0%,#a9a69c 38%,#c9b99d 62%,#e4d6bd 100%)}
.hero-shade{position:absolute;inset:0;background:linear-gradient(0deg,rgba(10,20,40,.72) 0%,rgba(10,20,40,.25) 55%,rgba(10,20,40,0) 100%)}
.hero-copy{position:absolute;left:22px;top:250px;color:#fff;max-width:600px}
.hero-copy h1{font-size:50px;line-height:1.15;font-weight:700}
.hero-copy p{margin-top:22px;font-size:17px;line-height:1.5;opacity:.9;max-width:470px}

.story{height:820px;background:var(--cream);position:relative}
.story-text{position:absolute;left:64px;top:220px;width:500px}
.eyebrow{font-size:12px;font-weight:800;letter-spacing:2px;color:var(--muted);text-transform:uppercase}
.story-text h2{font-size:40px;line-height:1.2;color:var(--navy);margin:22px 0 26px}
.story-text p{font-size:16px;line-height:1.7;color:var(--muted);margin-bottom:20px}
.story-photo{position:absolute;left:620px;top:80px;width:560px;height:692px;border-radius:8px;overflow:hidden;background:linear-gradient(180deg,#1f2a44 0%,#7a4a3c 42%,#e08a3a 58%,#2a1d1d 74%,#0e0d10 100%)}
.story-photo .caption{position:absolute;left:0;right:0;bottom:72px;text-align:center;color:#fff;font-weight:700;letter-spacing:4px;font-size:18px}
.story-photo .caption small{display:block;margin-top:10px;font-size:11px;letter-spacing:2px;opacity:.7}
.years-badge{position:absolute;left:600px;top:708px;width:212px;height:84px;background:var(--gold);border-radius:4px;padding:18px 22px;color:var(--navy-deep)}
.years-badge strong{display:block;font-family:"Playfair Display",Georgia,serif;font-size:26px}
.years-badge span{font-size:11px;font-weight:700}

.why{height:720px;background:var(--paper);text-align:center;padding-top:110px}
.why h2{font-size:42px;color:var(--navy)}
.why .lead{margin:18px auto 0;font-size:17px;color:var(--muted);max-width:560px;line-height:1.5}
.cards{display:flex;gap:30px;justify-content:center;margin-top:50px}
.card{width:360px;height:320px;background:var(--cream);border-radius:8px;padding:40px 42px}
.card .icon{width:56px;height:56px;border-radius:50%;margin:0 auto 24px;display:flex;align-items:center;justify-content:center}
.card h3{font-size:24px;color:var(--navy);margin-bottom:16px}
.card p{font-size:15px;line-height:1.6;color:var(--muted)}

.cta-wrap{height:440px;padding:0 20px}
.cta{height:372px;background:var(--navy);border-radius:14px;text-align:center;color:#fff;padding-top:80px;position:relative;overflow:hidden}
.cta::after{content:"";position:absolute;left:-140px;bottom:-220px;width:460px;height:460px;border-radius:50%;background:rgba(255,255,255,.04)}
.cta h2{font-size:40px}
.cta p{margin:20px auto 0;font-size:17px;opacity:.85;max-width:620px;line-height:1.5}
.cta-actions{margin-top:44px;display:flex;justify-content:center;gap:24px;position:relative;z-index:1}
.btn{display:inline-block;width:180px;padding:15px 0;border-radius:6px;font-weight:700;font-size:16px}
.btn-gold{background:var(--gold);color:var(--navy-deep)}
.btn-ghost{border:2px solid #fff;color:#fff}

.site-footer{height:312px;background:var(--stone);padding:50px 24px 0;position:relative}
.footer-grid{display:flex}
.footer-brand{width:300px}
.footer-brand .brand{font-size:40px;line-height:1.15}
.footer-brand p{margin-top:14px;font-size:15px;color:var(--muted)}
.footer-col{margin-left:0}
.footer-col h4{font-size:12px;font-weight:800;color:var(--ink);margin-bottom:14px;letter-spacing:.5px}
.footer-col li{list-style:none;font-size:15px;color:var(--muted);margin-bottom:12px}
.socials{display:flex;gap:12px}
.socials span{width:26px;height:26px;border-radius:50%;background:#4a5160;display:block}
.copyright{position:absolute;left:0;right:0;bottom:18px;text-align:center;font-size:11px;color:#8a8f99;border-top:1px solid var(--line);padding-top:14px;margin:0 24px}
</style>
</head>
<body>

<header class="site-nav">
  <div class="brand">Wander Lane Travel</div>
  <nav class="nav-links">
    <span>Brambleton Vacations</span>
    <span>Family Trips</span>
    <span>Texas Road Trips</span>
    <span>Destinations</span>
    <span class="active">About Us</span>
    <span class="nav-cta">Contact Us</span>
  </nav>
</header>

<section class="hero">
  <div class="hero-photo" role="img" aria-label="Smiling travel consultant standing on a sunny European street with balconied buildings"></div>
  <div class="hero-shade"></div>
  <div class="hero-copy">
    <h1>Crafting Magic Beyond the Screen</h1>
    <p>Meet the experts who turn your "Once upon a time" into your family's favorite reality.</p>
  </div>
</section>

<section class="story">
  <div class="story-text">
    <div class="eyebrow">Our Story</div>
    <h2>Local Roots, Global Wanderlust</h2>
    <p>Based in the heart of Texas, we started Wander Lane Travel with a simple observation: planning a family vacation shouldn't feel like a second job. As travel-obsessed parents ourselves, we spent years navigating the complexities of Brambleton, European rail systems, and finding the perfect Hill Country hidden gems.</p>
    <p>We realized that what families truly need isn't just a booking engine—it's a partner. Someone who knows which Brambleton resort has the best character breakfast and which road trip route through West Texas avoids the boredom. We combine professional travel expertise with the personable touch of a trusted friend.</p>
  </div>
  <div class="story-photo" role="img" aria-label="Silhouette of a family watching a sunset over the hills">
    <div class="caption">ABOUT US<small>SINCE DAY ONE</small></div>
  </div>
  <div class="years-badge"><strong>10+ Years</strong><span>Of Family Travel Expertise</span></div>
</section>

<section class="why">
  <h2>Why Wander With Us?</h2>
  <p class="lead">Our principles ensure your travel experience is as seamless as it is magical.</p>
  <div class="cards">
    <div class="card">
      <div class="icon" style="background:#dfe4ec">
        <svg width="24" height="24" viewBox="0 0 24 24" fill="none" stroke="#0f2444" stroke-width="2"><path d="M12 3l7 3v5c0 5-3 8-7 10-4-2-7-5-7-10V6z"/><path d="M9 12l2 2 4-4"/></svg>
      </div>
      <h3>Unwavering Trust</h3>
      <p>We treat your vacation budget like our own, ensuring every dollar spent delivers maximum value and lifelong memories.</p>
    </div>
    <div class="card">
      <div class="icon" style="background:#fbe6c4">
        <svg width="24" height="24" viewBox="0 0 24 24" fill="#f5a623"><path d="M12 2l2 7 7 3-7 3-2 7-2-7-7-3 7-3z"/></svg>
      </div>
      <h3>Personal Touch</h3>
      <p>No cookie-cutter itineraries. We learn your family's quirks, dietary needs, and sleep schedules to build the perfect plan.</p>
    </div>
    <div class="card">
      <div class="icon" style="background:#dfe4ec">
        <svg width="24" height="24" viewBox="0 0 24 24" fill="none" stroke="#0f2444" stroke-width="2"><circle cx="12" cy="9" r="6"/><path d="M8 14l-2 8 6-3 6 3-2-8"/></svg>
      </div>
      <h3>Expert Curation</h3>
      <p>Certified Brambleton Specialists and luxury travel advisors with the industry connections to get you the "extra" experiences.</p>
    </div>
  </div>
</section>

<section class="cta-wrap">
  <div class="cta">
    <h2>Ready to start your next chapter?</h2>
    <p>Whether it's a first Brambleton trip or a coastal retreat, our team is ready to guide you home.</p>
    <div class="cta-actions">
      <span class="btn btn-gold">Meet the Team</span>
      <span class="btn btn-ghost">Contact Us</span>
    </div>
  </div>
</section>

<footer class="site-footer">
  <div class="footer-grid">
    <div class="footer-brand">
      <div class="brand">Wander Lane<br>Travel</div>
      <p>Professional Family Travel Consultants</p>
    </div>
    <div class="footer-col" style="margin-left:0">
      <h4>Explore</h4>
      <ul><li>Brambleton Vacations</li><li>Texas Road Trips</li><li>Family Travel Tips</li></ul>
    </div>
    <div class="footer-col" style="margin-left:130px">
      <h4>Company</h4>
      <ul><li>About Our Team</li><li>Contact Us</li><li>Privacy Policy</li></ul>
    </div>
    <div class="footer-col" style="margin-left:170px">
      <h4>Connect</h4>
      <div class="socials"><span></span><span></span><span></span></div>
    </div>
  </div>
  <div class="copyright">© 2024 Wander Lane Travel. All rights reserved.</div>
</footer>

</body>
</html>
```